Harbor Stoneworks Business card logo

We are a tile and natural stone installation company with an emphasis on high quality and design assistance. I prefer a black background with a graphic logo or maybe a photo that gives a feel of tile/natural stone. I like bold, but tasteful colors. Something to really catch the eye without being gaudy. The final design should convey expert quality and attention to detail.

Contact Information for Business Card

HARBOR STONEWORKS Quality Design and Installation

Font styles to use
Other font styles liked:
• Graviton, Illegal curves

Requirements
Must have
• Business card must be an eye-catcher, but tasteful.
• Information I need on the card:
• Business name and tagline
• Neil Ashcombe, owner
• Phone: (xxx) xxx-xxxx
• Email
• Website

```html
<!DOCTYPE html>
<html lang="en">
<head>
<meta charset="utf-8">
<title>Harbor Stoneworks – Business Card</title>
<link rel="stylesheet" href="https://fonts.googleapis.com/css2?family=Quicksand:wght@500;700&display=swap">
<style>
  :root {
    --stone-light: #d8d3c2;
    --stone-mid: #b7b2a0;
    --stone-shadow: #8e8a7c;
    --card-black: #000000;
    --brand-teal: #1e8c70;
    --text-white: #ffffff;
  }
  html, body {
    margin: 0;
    padding: 0;
    overflow: hidden;
    background: var(--card-black);
  }
  .card {
    position: relative;
    width: 1200px;
    height: 708px;
    overflow: hidden;
    font-family: "Quicksand", sans-serif;
    color: var(--text-white);
  }
  .stone-backdrop {
    position: absolute;
    inset: 0;
    background:
      linear-gradient(180deg, rgba(0,0,0,0) 0%, rgba(0,0,0,0) 62%, rgba(0,0,0,0.55) 80%, var(--card-black) 100%),
      linear-gradient(180deg, var(--stone-light) 0%, var(--stone-mid) 40%, var(--stone-shadow) 47%, var(--stone-mid) 52%, var(--stone-light) 75%);
  }
  .brand-name {
    position: absolute;
    left: 0;
    right: 0;
    top: 52px;
    margin: 0;
    text-align: center;
    font-weight: 700;
    color: var(--brand-teal);
    line-height: 1;
  }
  .brand-name .line-one {
    display: block;
    font-size: 140px;
    letter-spacing: 6px;
  }
  .brand-name .line-two {
    display: block;
    margin-top: 14px;
    font-size: 104px;
    letter-spacing: 2px;
  }
  .tagline {
    position: absolute;
    left: 0;
    right: 0;
    top: 334px;
    margin: 0;
    text-align: center;
    font-size: 48px;
    font-weight: 700;
  }
  .website {
    position: absolute;
    left: 0;
    right: 0;
    top: 400px;
    margin: 0;
    text-align: center;
    font-size: 76px;
    font-weight: 700;
    letter-spacing: 1px;
  }
  .contact {
    position: absolute;
    left: 61px;
    top: 516px;
    margin: 0;
    padding: 0;
    list-style: none;
    font-size: 35px;
    font-weight: 500;
    line-height: 49px;
  }
</style>
</head>
<body>
  <div class="card">
    <div class="stone-backdrop" role="img" aria-label="Close-up photograph of textured natural stone tiles in warm beige and grey, fading to black at the bottom"></div>

    <h1 class="brand-name">
      <span class="line-one">HARBOR</span>
      <span class="line-two">STONEWORKS</span>
    </h1>

    <p class="tagline">Quality Design and Installation</p>
    <p class="website">www.harborstoneworks.com</p>

    <ul class="contact">
      <li>N: Neil Ashcombe</li>
      <li>P:&nbsp; 555-014-2290</li>
      <li>E: neil.a@harborstoneworks.com</li>
    </ul>
  </div>
</body>
</html>
```